Quill And Ferry Business Card

I need a business card designed around my logo (which was designed here on Sketch Forum!)

Target Market(s)

Professional Businesses

Industry/Entity Type

Business

Requirements
Must have
• Details that must be on the business card:

Renata Ovalle
Director
0491 253 608
renata@quillandferry.com.au
www.quillandferry.com.au
PO Box 4720 Harlow Ridge Vic 3981

```html
<!DOCTYPE html>
<html lang="en">
<head>
<meta charset="utf-8">
<title>Quill And Ferry Business Card</title>
<link rel="stylesheet" href="https://fonts.googleapis.com/css2?family=Cinzel:wght@400;700&family=Tinos:wght@400;700&display=swap">
<style>
  :root {
    --page: #ecebe8;
    --card: #ffffff;
    --ink: #1c1c1c;
    --red: #c8202a;
    --rule: #222222;
    --shadow: rgba(0, 0, 0, 0.18);
  }
  * { margin: 0; padding: 0; box-sizing: border-box; }
  html, body {
    width: 1200px;
    height: 646px;
    overflow: hidden;
    background: var(--page);
  }
  .canvas { position: relative; width: 1200px; height: 646px; }
  .card {
    position: absolute;
    top: 173px;
    width: 520px;
    height: 300px;
    background: var(--card);
    box-shadow: 0 6px 18px var(--shadow);
    overflow: hidden;
  }
  .card--front { left: 50px; }
  .card--back { left: 630px; }

  /* Front */
  .front-arc {
    position: absolute;
    left: 0;
    top: 0;
    width: 520px;
    height: 300px;
  }
  .brand {
    position: absolute;
    left: 56px;
    top: 112px;
    display: flex;
    align-items: center;
    gap: 16px;
  }
  .brand__mark { width: 36px; height: 36px; background: var(--red); }
  .brand__name {
    font-family: "Cinzel", serif;
    font-size: 32px;
    letter-spacing: 1px;
    color: var(--ink);
    line-height: 1;
  }
  .brand__tagline {
    position: absolute;
    left: 108px;
    top: 154px;
    font-family: "Cinzel", serif;
    font-size: 13px;
    letter-spacing: 3px;
    color: var(--red);
    text-transform: uppercase;
  }

  /* Back */
  .person { position: absolute; left: 34px; top: 52px; font-family: "Cinzel", serif; }
  .person__name { font-weight: 700; font-size: 21px; color: var(--ink); letter-spacing: 0.5px; }
  .person__role { margin-top: 4px; margin-left: 120px; font-size: 13px; color: var(--ink); }
  .contacts {
    position: absolute;
    left: 34px;
    top: 178px;
    list-style: none;
    font-family: "Tinos", serif;
    font-size: 12.5px;
    color: var(--ink);
  }
  .contacts__item { display: flex; align-items: center; gap: 9px; line-height: 18px; }
  .contacts__item--bold { font-weight: 700; }
  .contacts__icon { width: 11px; height: 11px; flex: none; }
  .divider {
    position: absolute;
    left: 268px;
    top: 26px;
    width: 1.5px;
    height: 196px;
    background: var(--rule);
  }
  .back-brand {
    position: absolute;
    left: 292px;
    top: 84px;
    display: flex;
    align-items: center;
    gap: 12px;
  }
  .back-brand__mark { width: 30px; height: 30px; background: var(--red); }
  .back-brand__name { font-family: "Cinzel", serif; font-size: 18px; color: var(--ink); letter-spacing: 0.5px; }
  .address {
    position: absolute;
    right: 22px;
    bottom: 26px;
    font-family: "Cinzel", serif;
    font-size: 13.5px;
    color: var(--ink);
    letter-spacing: 0.3px;
  }
</style>
</head>
<body>
<main class="canvas">
  <section class="card card--front" aria-label="Card front">
    <svg class="front-arc" viewBox="0 0 520 300" aria-hidden="true">
      <path d="M250 300 C420 250 470 120 430 0 L452 0 C500 130 440 265 280 300 Z" fill="#1c1c1c"/>
    </svg>
    <div class="brand">
      <span class="brand__mark"></span>
      <span class="brand__name">Quill And Ferry</span>
    </div>
    <p class="brand__tagline">Ledgers kept simple</p>
  </section>

  <section class="card card--back" aria-label="Card back">
    <div class="person">
      <p class="person__name">Renata Ovalle</p>
      <p class="person__role">Director</p>
    </div>
    <ul class="contacts">
      <li class="contacts__item">
        <svg class="contacts__icon" viewBox="0 0 12 12" aria-hidden="true"><path d="M2 1l2 0 1 3-1.5 1a7 7 0 0 0 3.5 3.5L8 7l3 1v2a1 1 0 0 1-1 1A9 9 0 0 1 1 2a1 1 0 0 1 1-1z" fill="#1c1c1c"/></svg>
        <span>0491 253 608</span>
      </li>
      <li class="contacts__item contacts__item--bold">
        <svg class="contacts__icon" viewBox="0 0 12 12" aria-hidden="true"><rect x="0.5" y="2.5" width="11" height="7.5" fill="none" stroke="#1c1c1c"/><path d="M0.5 2.5L6 7l5.5-4.5" fill="none" stroke="#1c1c1c"/></svg>
        <span>renata@quillandferry.com.au</span>
      </li>
      <li class="contacts__item contacts__item--bold">
        <svg class="contacts__icon" viewBox="0 0 12 12" aria-hidden="true"><circle cx="6" cy="6" r="5.2" fill="none" stroke="#1c1c1c"/><ellipse cx="6" cy="6" rx="2.2" ry="5.2" fill="none" stroke="#1c1c1c"/><path d="M0.8 6h10.4" stroke="#1c1c1c"/></svg>
        <span>www.quillandferry.com.au</span>
      </li>
    </ul>
    <span class="divider"></span>
    <div class="back-brand">
      <span class="back-brand__mark"></span>
      <span class="back-brand__name">Quill And Ferry</span>
    </div>
    <p class="address">PO Box 4720 Harlow Ridge Vic 3981</p>
  </section>
</main>
</body>
</html>
```